Brochure 11 x 25.5 Trifold

Harborline Staffing Works, Inc. is a payroll, benefits, and HR administration company. We are in need of a brochure to showcase all of our services. Attached is a one-page information sheet that contains the information we want in the brochure as well as several images. The brochure is a 11 x 25.5 tri-fold (a sample is attached). Please use the colors in the attached logo and design to complement our website harborlineworks.example.
Target Market(s)
Company executives
Industry/Entity Type
Human Resource Management
Other font styles liked:
- Avenir LT

```html
<!DOCTYPE html>
<html lang="en">
<head>
<meta charset="utf-8">
<title>Harborline Staffing Works – Trifold Brochure</title>
<link href="https://fonts.googleapis.com/css2?family=Montserrat:wght@400;500;600;700;800&display=swap" rel="stylesheet">
<style>
:root{
  --navy:#1e3a6b;
  --navy-deep:#142a52;
  --green:#8dc63f;
  --green-dark:#6ea52c;
  --ink:#3c4450;
  --muted:#7a818c;
  --paper:#ffffff;
  --backdrop:#e9ebee;
  --photo-a:#8a97a8;
  --photo-b:#cfd6de;
  --line:#d8dde3;
}
*{box-sizing:border-box;margin:0;padding:0}
html,body{width:714px;height:1200px;overflow:hidden}
body{background:var(--backdrop);font-family:"Montserrat",Arial,sans-serif;color:var(--ink);position:relative}
.spread{position:absolute;left:27px;width:660px;height:285px;background:var(--paper);box-shadow:0 3px 10px rgba(0,0,0,.15);overflow:hidden}
.spread--outside{top:270px}
.spread--inside{top:645px}
.panel{position:absolute;top:0;width:220px;height:285px;overflow:hidden}
.panel--1{left:0}.panel--2{left:220px}.panel--3{left:440px}
.shapes{position:absolute;inset:0;width:220px;height:285px}
.photo{position:absolute;background:linear-gradient(135deg,var(--photo-a),var(--photo-b))}

/* brand */
.brand{position:absolute;display:flex;align-items:center;gap:4px;font-weight:700;font-size:6px;color:var(--navy);text-transform:uppercase;letter-spacing:.2px;line-height:1.1}
.brand__dot{width:9px;height:9px;border-radius:50%;background:var(--green);flex:none}

/* outside left */
.apart__title{position:absolute;left:14px;top:16px;font-size:11px;font-weight:800;line-height:1.05;color:var(--navy)}
.apart__title span{display:block;color:var(--green)}
.apart__grid{position:absolute;left:14px;top:54px;width:194px;display:grid;grid-template-columns:1fr 1fr;gap:14px 10px}
.feature{display:flex;gap:5px}
.feature__icon{width:16px;height:16px;border-radius:50%;background:var(--green);flex:none;display:flex;align-items:center;justify-content:center}
.feature__name{font-size:5.4px;font-weight:700;color:var(--navy);text-transform:uppercase}
.feature__text{font-size:4.6px;line-height:1.35;color:var(--muted);margin-top:1px}

/* outside middle */
.contact{position:absolute;left:16px;top:16px;width:190px}
.contact__label{font-size:8px;font-weight:800;color:var(--navy)}
.contact__name{font-size:6.5px;font-weight:700;color:var(--green);text-transform:uppercase;margin-top:2px;line-height:1.2}
.contact__list{list-style:none;margin-top:9px}
.contact__item{display:flex;align-items:center;gap:5px;font-size:5.4px;color:var(--ink);margin-bottom:6px;line-height:1.3}
.contact__icon{width:11px;height:11px;border-radius:50%;background:var(--navy);flex:none;display:flex;align-items:center;justify-content:center}

/* cover */
.cover__text{position:absolute;left:16px;top:206px;width:192px;text-align:right}
.cover__lead{font-size:7px;font-weight:700;color:var(--navy);line-height:1.25;text-transform:uppercase}
.cover__lead em{font-style:normal;color:var(--green)}
.cover__title{font-size:14px;font-weight:800;color:var(--navy);line-height:1.1;text-transform:uppercase;margin-top:2px}
.cover__web{position:absolute;left:40px;right:0;top:258px;height:14px;background:var(--green);color:#fff;font-size:6px;font-weight:700;display:flex;align-items:center;justify-content:center;letter-spacing:.3px}

/* inside left */
.hire__device{position:absolute;left:18px;top:120px;width:120px;height:60px;border-radius:3px;background:linear-gradient(160deg,#d9dee5,#f3f5f7);border:2px solid #444c57}
.hire__phone{position:absolute;left:126px;top:140px;width:28px;height:44px;border-radius:4px;background:linear-gradient(160deg,#d9dee5,#f3f5f7);border:2px solid #444c57}
.hire__title{position:absolute;left:16px;top:194px;font-size:12.5px;font-weight:800;line-height:1.05;color:var(--green);text-transform:uppercase}
.hire__title span{display:block}
.hire__sub{position:absolute;left:16px;top:222px;font-size:8px;font-weight:800;color:var(--navy);text-transform:uppercase;line-height:1.1}
.hire__text{position:absolute;left:16px;top:240px;width:186px;font-size:5px;line-height:1.45;color:var(--muted)}

/* inside middle */
.services__title{position:absolute;left:16px;top:16px;font-size:10px;font-weight:800;color:var(--navy);display:flex;align-items:center;gap:5px}
.services__title::before{content:"";width:4px;height:12px;background:var(--green)}
.services__list{position:absolute;left:16px;top:40px;width:190px;list-style:none;display:grid;grid-template-columns:1fr 1fr;gap:9px 8px}
.service{display:flex;align-items:center;gap:5px;font-size:5.4px;font-weight:600;color:var(--navy)}
.service__icon{width:12px;height:12px;background:var(--green);border-radius:2px;flex:none}
.services__cta{position:absolute;left:0;right:0;bottom:14px;height:16px;background:var(--green);color:#fff;font-size:5.8px;font-weight:700;text-transform:uppercase;display:flex;align-items:center;justify-content:center;letter-spacing:.3px}

/* inside right */
.cycle{position:absolute;left:10px;top:12px;width:200px;height:160px}
.cycle__node{font-family:"Montserrat",Arial,sans-serif;font-size:5.4px;font-weight:700;fill:var(--navy);text-transform:uppercase}
.cycle__center{font-family:"Montserrat",Arial,sans-serif;font-size:6px;font-weight:800;fill:var(--navy)}
</style>
</head>
<body>

<section class="spread spread--outside" aria-label="Brochure outside">

  <div class="panel panel--1">
    <h2 class="apart__title">WHAT <span>SETS US APART?</span></h2>
    <div class="apart__grid">
      <div class="feature"><div class="feature__icon"><svg width="8" height="8" viewBox="0 0 8 8"><path d="M1 4l2 2 4-4" stroke="#fff" stroke-width="1.3" fill="none"/></svg></div><div><div class="feature__name">One Partner</div><p class="feature__text">One contact for all HR.</p></div></div>
      <div class="feature"><div class="feature__icon"><svg width="8" height="8" viewBox="0 0 8 8"><path d="M1 4l2 2 4-4" stroke="#fff" stroke-width="1.3" fill="none"/></svg></div><div><div class="feature__name">Local Experts</div><p class="feature__text">Specialists who know your market.</p></div></div>
      <div class="feature"><div class="feature__icon"><svg width="8" height="8" viewBox="0 0 8 8"><path d="M1 4l2 2 4-4" stroke="#fff" stroke-width="1.3" fill="none"/></svg></div><div><div class="feature__name">Secure Data</div><p class="feature__text">Protected records at every step.</p></div></div>
      <div class="feature"><div class="feature__icon"><svg width="8" height="8" viewBox="0 0 8 8"><path d="M1 4l2 2 4-4" stroke="#fff" stroke-width="1.3" fill="none"/></svg></div><div><div class="feature__name">Fast Payroll</div><p class="feature__text">Accurate pay on every cycle.</p></div></div>
      <div class="feature"><div class="feature__icon"><svg width="8" height="8" viewBox="0 0 8 8"><path d="M1 4l2 2 4-4" stroke="#fff" stroke-width="1.3" fill="none"/></svg></div><div><div class="feature__name">Compliance</div><p class="feature__text">Rules tracked so you don't.</p></div></div>
      <div class="feature"><div class="feature__icon"><svg width="8" height="8" viewBox="0 0 8 8"><path d="M1 4l2 2 4-4" stroke="#fff" stroke-width="1.3" fill="none"/></svg></div><div><div class="feature__name">Real Support</div><p class="feature__text">People answer when you call.</p></div></div>
    </div>
    <svg class="shapes" viewBox="0 0 220 285" aria-hidden="true">
      <path d="M0 232 C70 205 150 215 220 190 L220 206 C150 230 70 222 0 248 Z" fill="var(--green)"/>
      <path d="M0 252 C70 228 150 236 220 212 L220 285 L0 285 Z" fill="var(--navy)"/>
    </svg>
  </div>

  <div class="panel panel--2">
    <div class="contact">
      <div class="contact__label">CONTACT</div>
      <div class="contact__name">Harborline Staffing Works, Inc.</div>
      <ul class="contact__list">
        <li class="contact__item"><span class="contact__icon"><svg width="6" height="6" viewBox="0 0 6 6"><path d="M1 1h1.2l.6 1.4-.8.5a3 3 0 0 0 1.1 1.1l.5-.8L5 3.8V5C2.8 5 1 3.2 1 1z" fill="#fff"/></svg></span>(225) 555-0147</li>
        <li class="contact__item"><span class="contact__icon"><svg width="6" height="6" viewBox="0 0 6 6"><rect x=".6" y="1.4" width="4.8" height="3.4" fill="none" stroke="#fff" stroke-width=".7"/><path d="M.6 1.5 3 3.3l2.4-1.8" fill="none" stroke="#fff" stroke-width=".7"/></svg></span>info@harborlineworks.example</li>
        <li class="contact__item"><span class="contact__icon"><svg width="6" height="6" viewBox="0 0 6 6"><circle cx="3" cy="3" r="2.2" fill="none" stroke="#fff" stroke-width=".7"/><path d="M.8 3h4.4M3 .8v4.4" stroke="#fff" stroke-width=".5"/></svg></span>www.harborlineworks.example</li>
        <li class="contact__item"><span class="contact__icon"><svg width="6" height="6" viewBox="0 0 6 6"><path d="M3 5.4S1.2 3.6 1.2 2.4a1.8 1.8 0 0 1 3.6 0C4.8 3.6 3 5.4 3 5.4z" fill="#fff"/></svg></span>418 Quayside Drive,<br>Port Avery, LA 70000</li>
      </ul>
    </div>
    <svg class="shapes" viewBox="0 0 220 285" aria-hidden="true">
      <path d="M0 246 C40 230 70 150 150 150 L220 140 L220 152 L150 162 C80 166 50 240 0 262 Z" fill="var(--green)"/>
      <path d="M0 222 C30 200 60 150 120 140 L220 122 L220 132 L120 150 C70 160 40 206 0 234 Z" fill="var(--navy)"/>
    </svg>
    <div class="photo" role="img" aria-label="Photo of two business people shaking hands" style="left:62px;top:150px;width:100px;height:100px;border-radius:50%;border:4px solid #fff"></div>
    <div class="brand" style="left:70px;top:262px"><span class="brand__dot"></span>Harborline Staffing Works, Inc.</div>
  </div>

  <div class="panel panel--3">
    <div class="brand" style="right:12px;top:10px"><span class="brand__dot"></span>Harborline Staffing<br>Works, Inc.</div>
    <svg class="shapes" viewBox="0 0 220 285">
      <defs><linearGradient id="coverPhoto" x1="0" y1="0" x2="1" y2="1"><stop offset="0" stop-color="#7d8b9e"/><stop offset="1" stop-color="#d4dae1"/></linearGradient></defs>
      <path role="img" aria-label="Photo of a business team meeting around a table" d="M0 32 H220 V150 C160 190 70 180 0 150 Z" fill="url(#coverPhoto)"/>
      <path d="M0 150 C70 180 160 190 220 150 L220 162 C160 200 70 192 0 164 Z" fill="var(--green)"/>
      <path d="M0 120 C10 140 30 150 40 150 L0 170 Z" fill="var(--navy)"/>
      <path d="M0 164 C70 192 160 200 220 162 L220 170 C160 208 70 200 0 172 Z" fill="var(--navy)"/>
    </svg>
    <div class="cover__text">
      <p class="cover__lead">Your <em>single-source</em><br>solution for the</p>
      <h1 class="cover__title">Entire Employee</h1>
    </div>
    <div class="cover__web">www.harborlineworks.example</div>
  </div>
</section>

<section class="spread spread--inside" aria-label="Brochure inside">

  <div class="panel panel--1">
    <svg class="shapes" viewBox="0 0 220 285">
      <defs><linearGradient id="hirePhoto" x1="0" y1="0" x2="1" y2="1"><stop offset="0" stop-color="#7d8b9e"/><stop offset="1" stop-color="#d4dae1"/></linearGradient></defs>
      <path role="img" aria-label="Photo of colleagues working together in an office" d="M0 0 H220 V88 C150 118 60 112 0 96 Z" fill="url(#hirePhoto)"/>
      <path d="M0 96 C60 112 150 118 220 88 V100 C150 130 60 124 0 108 Z" fill="var(--green)"/>
      <path d="M0 108 C60 124 150 130 220 100 V106 C150 136 60 130 0 114 Z" fill="var(--navy)"/>
    </svg>
    <div class="hire__device" role="img" aria-label="Laptop showing the online payroll portal"></div>
    <div class="hire__phone" role="img" aria-label="Phone showing the mobile employee app"></div>
    <h2 class="hire__title"><span>From hire</span><span>to retire,</span></h2>
    <p class="hire__sub">We've got you covered</p>
    <p class="hire__text">From first hire to final paycheck, we handle payroll, benefits and HR so your team can focus on growth.</p>
  </div>

  <div class="panel panel--2">
    <h2 class="services__title">OUR SERVICES</h2>
    <ul class="services__list">
      <li class="service"><span class="service__icon"></span>Payroll</li>
      <li class="service"><span class="service__icon"></span>Benefits</li>
      <li class="service"><span class="service__icon"></span>HR Administration</li>
      <li class="service"><span class="service__icon"></span>Compliance</li>
      <li class="service"><span class="service__icon"></span>Onboarding</li>
      <li class="service"><span class="service__icon"></span>Time Tracking</li>
      <li class="service"><span class="service__icon"></span>Workers' Comp</li>
      <li class="service"><span class="service__icon"></span>Retirement Plans</li>
      <li class="service"><span class="service__icon"></span>Recruiting</li>
      <li class="service"><span class="service__icon"></span>Training</li>
      <li class="service"><span class="service__icon"></span>Employee Relations</li>
      <li class="service"><span class="service__icon"></span>Tax Filing</li>
      <li class="service"><span class="service__icon"></span>Reporting</li>
      <li class="service"><span class="service__icon"></span>Offboarding</li>
      <li class="service"><span class="service__icon"></span>Self-Service Portal</li>
      <li class="service"><span class="service__icon"></span>Consulting</li>
    </ul>
    <div class="services__cta">Call today for a free consultation</div>
  </div>

  <div class="panel panel--3">
    <svg class="cycle" viewBox="0 0 200 160" aria-label="Employee lifecycle diagram">
      <circle cx="100" cy="80" r="52" fill="none" stroke="var(--line)" stroke-width="1.5"/>
      <circle cx="100" cy="80" r="26" fill="#fff" stroke="var(--green)" stroke-width="2"/>
      <text class="cycle__center" x="100" y="78" text-anchor="middle">EMPLOYEE</text>
      <text class="cycle__center" x="100" y="86" text-anchor="middle">LIFECYCLE</text>
      <g fill="var(--green)">
        <circle cx="100" cy="28" r="5"/><circle cx="145" cy="54" r="5" fill="var(--navy)"/><circle cx="145" cy="106" r="5"/>
        <circle cx="100" cy="132" r="5" fill="var(--navy)"/><circle cx="55" cy="106" r="5"/><circle cx="55" cy="54" r="5" fill="var(--navy)"/>
      </g>
      <text class="cycle__node" x="100" y="17" text-anchor="middle">Recruit</text>
      <text class="cycle__node" x="154" y="56">Hire</text>
      <text class="cycle__node" x="154" y="108">Onboard</text>
      <text class="cycle__node" x="100" y="148" text-anchor="middle">Pay</text>
      <text class="cycle__node" x="46" y="108" text-anchor="end">Develop</text>
      <text class="cycle__node" x="46" y="56" text-anchor="end">Retire</text>
    </svg>
    <svg class="shapes" viewBox="0 0 220 285">
      <defs><linearGradient id="teamPhoto" x1="0" y1="0" x2="1" y2="1"><stop offset="0" stop-color="#7d8b9e"/><stop offset="1" stop-color="#d4dae1"/></linearGradient></defs>
      <path d="M0 186 C70 172 150 176 220 196 V206 C150 186 70 182 0 196 Z" fill="var(--green)"/>
      <path d="M0 196 C70 182 150 186 220 206 V212 C150 192 70 188 0 202 Z" fill="var(--navy)"/>
      <path role="img" aria-label="Photo of a team in a business meeting" d="M0 202 C70 188 150 192 220 212 V285 H0 Z" fill="url(#teamPhoto)"/>
    </svg>
  </div>
</section>

</body>
</html>
```